Salon and Spa Distributor Business Card

Need a business card. We are are distributor in the salon and spa industry. We identify with natural beauty. Need a card with:
Company Name: Petal Haven"
Title: "President & CEO"
Address
Company Phone number
email
website
Tag Line:" The Professional Salon Source"

Industry/Entity Type

Business

Contact Information for Business Card

Name: Lena Morcott
Title: "President & CEO"
Address: 317 Birchfield Ln, Oakvane, NJ 07481
Company Phone number: 800-463-9152
email: lenamorcott@petalhaven-example.com
website: www.petalhaven-example.com

Requirements
Should not have
• No black backgrounds

```html
<!DOCTYPE html>
<html lang="en">
<head>
<meta charset="utf-8">
<title>Petal Haven – Business Card</title>
<link href="https://fonts.googleapis.com/css2?family=Questrial&family=Open+Sans:wght@400;600;700&display=swap" rel="stylesheet">
<style>
  :root {
    --page-bg: #d9dbd9;
    --card-bg: #f4f6f2;
    --ink-dark: #2b2d2c;
    --ink-name: #6d716e;
    --leaf-light: #8fcf94;
    --leaf-mid: #5fb55f;
    --leaf-deep: #3e9a3c;
    --brand-green: #5cae62;
    --rule-green: #4fae4a;
  }
  * { margin: 0; padding: 0; box-sizing: border-box; }
  html, body { width: 1200px; height: 727px; overflow: hidden; }
  body {
    background: var(--page-bg);
    font-family: "Open Sans", Arial, sans-serif;
    position: relative;
  }
  .card {
    position: absolute;
    left: 100px; top: 78px;
    width: 1000px; height: 571px;
    background: var(--card-bg);
    border-radius: 6px;
    box-shadow: 0 10px 30px rgba(0,0,0,.18);
    overflow: hidden;
  }
  .card__artwork {
    position: absolute;
    left: 40px; top: 70px;
    width: 290px; height: 420px;
    border-radius: 40% 55% 30% 45%;
    background: linear-gradient(150deg, var(--leaf-light) 0%, var(--leaf-mid) 55%, var(--leaf-deep) 100%);
  }
  .brand {
    position: absolute;
    left: 345px; top: 92px;
  }
  .brand__name {
    font-family: "Questrial", Arial, sans-serif;
    font-size: 76px;
    font-weight: 400;
    line-height: 1;
    color: var(--brand-green);
    letter-spacing: 1px;
  }
  .brand__tagline {
    margin-top: 4px;
    margin-left: 8px;
    font-family: "Questrial", Arial, sans-serif;
    font-size: 24px;
    color: var(--ink-dark);
  }
  .card__rule {
    position: absolute;
    left: 610px; top: 262px;
    width: 390px; height: 3px;
    background: var(--rule-green);
  }
  .person {
    position: absolute;
    left: 345px; top: 236px;
  }
  .person__name {
    font-size: 34px;
    line-height: 1.1;
    color: var(--ink-dark);
    white-space: nowrap;
  }
  .person__name strong { color: var(--ink-name); font-weight: 700; }
  .person__title {
    font-size: 24px;
    font-weight: 600;
    color: var(--rule-green);
  }
  .contacts {
    position: absolute;
    left: 355px; top: 340px;
    list-style: none;
    font-size: 20px;
    color: var(--ink-dark);
  }
  .contacts__row { display: flex; align-items: center; gap: 28px; height: 42px; }
  .contacts__item { display: flex; align-items: center; gap: 12px; white-space: nowrap; }
  .contacts__icon { width: 20px; height: 20px; fill: var(--rule-green); flex: none; }
</style>
</head>
<body>
  <main class="card">
    <div class="card__artwork" role="img" aria-label="Illustration of a woman in profile with flowing green hair and leaves"></div>

    <header class="brand">
      <h1 class="brand__name">Petal Haven</h1>
      <p class="brand__tagline">The Professional Salon Source</p>
    </header>

    <div class="card__rule"></div>

    <section class="person">
      <p class="person__name">Lena <strong>Morcott</strong></p>
      <p class="person__title">President &amp; CEO</p>
    </section>

    <ul class="contacts">
      <li class="contacts__row">
        <span class="contacts__item">
          <svg class="contacts__icon" viewBox="0 0 20 20" aria-hidden="true"><path d="M10 1a6 6 0 0 0-6 6c0 4.5 6 12 6 12s6-7.5 6-12a6 6 0 0 0-6-6zm0 8.5A2.5 2.5 0 1 1 10 4.5a2.5 2.5 0 0 1 0 5z"/></svg>
          317 Birchfield Ln, Oakvane, NJ 07481
        </span>
      </li>
      <li class="contacts__row">
        <span class="contacts__item">
          <svg class="contacts__icon" viewBox="0 0 20 20" aria-hidden="true"><path d="M2 6c0-2 3-3 8-3s8 1 8 3v2h-4V6.5h-8V8H2zM5 9h10l2 8H3z"/></svg>
          800-463-9152
        </span>
        <span class="contacts__item">
          <svg class="contacts__icon" viewBox="0 0 20 20" aria-hidden="true"><path d="M1 4h18v12H1zM2.5 5.5 10 11l7.5-5.5v-.1h-15z"/></svg>
          lenamorcott@petalhaven-example.com
        </span>
      </li>
      <li class="contacts__row">
        <span class="contacts__item">
          <svg class="contacts__icon" viewBox="0 0 20 20" aria-hidden="true"><path d="M10 1a9 9 0 1 0 0 18 9 9 0 0 0 0-18zm0 1.6c.9.9 1.7 2.5 2 4.4H8c.3-1.9 1.1-3.5 2-4.4zM7.8 8.5h4.4a15 15 0 0 1 0 3H7.8a15 15 0 0 1 0-3zM2.7 8.5h3.6a16 16 0 0 0 0 3H2.7a7.4 7.4 0 0 1 0-3zm11 0h3.6a7.4 7.4 0 0 1 0 3h-3.6a16 16 0 0 0 0-3zM8 13h4c-.3 1.9-1.1 3.5-2 4.4-.9-.9-1.7-2.5-2-4.4z"/></svg>
          www.petalhaven-example.com
        </span>
      </li>
    </ul>
  </main>
</body>
</html>
```